Corvenna Building Inspections, Estimating & Project Management

Please read my capability statement uploaded in the files to get an indepth overview of who we are and what we do.
We are a construction company that is moving away from onsite construction to consultancy and inspection services. We will offer Building Inspections, Estimating Services, Project Management and Construction Management. We will still be working out in the field, however as inspectors and and coordinators only.
I am looking to build a website from scratch. I already have my logo built by sketch hive previously and wish to remove the company slogan "Frameworks & Outcomes".
Background: Corvenna Pty Ltd is in the process of shutting down and re-registering as Corvenna Australia Pty Ltd. It will however retain all the original logos.
I do like websites like https://ridgeline.tolvexsite-demo.com/#
I also do like to write all my emails in Roboto-Light font and open to suggestions on it's usage.
I currently host with Southland Webhouse and they use Wordpress 5.0

Home Owners Building or Renovating, Realestate Agents, Commercial Builders, Trades that require Estimating,

• All fonts have been uploaded.

• Must have the ability for monthly updates, photo uploads and industry tips I can share. A page dedicated to tips and understanding of what sets us apart from the competitors (this will require lots of input from me).
• I personally like pages like https://ridgeline.tolvexsite-demo.com/# which have a background image and the foreground scrolling past. Open to suggestions here. A website that sets me apart of Brisbane rivals
• Fixed pricing

```html
<!DOCTYPE html>
<html lang="en">
<head>
<meta charset="utf-8">
<title>Corvenna — Building Inspections, Estimating &amp; Project Management</title>
<link href="https://fonts.googleapis.com/css2?family=Plus+Jakarta+Sans:wght@400;500;600;700;800&display=swap" rel="stylesheet">
<style>
:root{
  --accent:#f9b21b;
  --navy:#132144;
  --navy-2:#1b2b52;
  --ink:#15203a;
  --muted:#5c6478;
  --sky:#eaf5fc;
  --line:#e4e8ef;
  --white:#ffffff;
}
*{margin:0;padding:0;box-sizing:border-box}
html,body{width:1200px;height:4488px;overflow:hidden}
body{position:relative;background:var(--white);font-family:"Plus Jakarta Sans",sans-serif;color:var(--ink)}
.abs{position:absolute}
.eyebrow{font-size:9px;font-weight:700;letter-spacing:1.6px;color:var(--accent);text-transform:uppercase}
.h2{font-size:35px;font-weight:700;letter-spacing:-1px;line-height:1.15;color:var(--ink)}
.lead{font-size:11px;line-height:18px;color:var(--muted)}
.center{left:0;width:1200px;text-align:center}
.btn{position:absolute;display:flex;align-items:center;justify-content:center;gap:6px;background:var(--accent);color:#fff;font-size:11px;font-weight:700;border-radius:4px}
.btn svg{width:12px;height:12px}
.photo{position:absolute;overflow:hidden}

/* hero */
.hero{left:25px;top:24px;width:1150px;height:540px;border-radius:30px;background:linear-gradient(180deg,#3d4d66 0%,#6b6258 45%,#b47a3a 80%,#8a5a2c 100%)}
.nav{left:80px;top:42px;width:1040px;height:34px;display:flex;align-items:center}
.brand{display:flex;align-items:center;gap:9px;font-size:25px;font-weight:800;color:#fff;letter-spacing:.5px}
.brand i{width:16px;height:16px;background:var(--accent);display:block}
.menu{position:absolute;left:320px;display:flex;gap:30px;font-size:11px;font-weight:500;color:#fff}
.menu .on{color:var(--accent)}
.hero-copy{color:#fff}
.hero h1{font-size:44px;font-weight:700;letter-spacing:-1.3px;line-height:49px}
.ghost{position:absolute;display:flex;align-items:center;justify-content:center;gap:6px;border:1px solid rgba(255,255,255,.8);color:#fff;font-size:11px;font-weight:700;border-radius:4px}

/* about */
.checks{left:603px;top:845px;width:400px;height:116px;background:var(--sky);border-radius:8px;padding:20px 20px}
.checks li{list-style:none;display:flex;align-items:center;gap:8px;font-size:11px;font-weight:500;height:29.5px}

/* cards */
.card{position:absolute;width:256px;height:310px;border:1px solid var(--line);border-radius:14px;background:#fff;padding:22px 19px}
.card h3{font-size:14px;font-weight:600;margin-top:22px}
.card p{font-size:10px;line-height:18px;color:var(--muted);margin-top:16px}
.card hr{border:0;border-top:1px solid var(--line);margin:14px 0 18px}
.card .num{font-size:33px;font-weight:600;letter-spacing:-1px;line-height:36px}
.card small{font-size:9.5px;color:var(--muted)}
.tile{position:absolute;width:256px;height:310px;border-radius:14px}

/* projects */
.projects{left:0;top:1963px;width:1200px;height:695px;background:var(--sky)}
.proj{position:absolute;top:2188px;width:276px;height:329px;border-radius:12px}
.proj span{position:absolute;left:25px;bottom:20px;font-size:13.5px;font-weight:700;color:#fff}

/* cta */
.cta{left:0;top:2658px;width:1200px;height:326px;background:var(--navy)}

/* blog */
.post{position:absolute;top:3207px;width:256px;height:274px;border:1px solid var(--line);border-radius:12px;background:#fff;overflow:hidden}
.post .img{height:165px}
.post h4{font-size:13.5px;font-weight:600;line-height:19px;margin:17px 18px 0}
.post a{display:flex;align-items:center;gap:4px;margin:10px 18px 0;font-size:10px;font-weight:600;color:var(--accent);text-decoration:none}

/* contact */
.contact{left:0;top:3550px;width:1200px;height:525px;background:var(--sky)}
.info{left:197px;top:3618px;width:256px;height:388px;border-radius:14px;background:var(--navy);color:#fff;text-align:center}
.form{left:472px;top:3622px;width:531px;height:382px;border-radius:14px;background:#fff}
.field{position:absolute;height:26px;border-bottom:1px solid var(--line);font-size:8.5px;color:#a4aab6;padding-top:3px}

/* footer */
.footer{left:0;top:4075px;width:1200px;height:413px;background:var(--navy);color:#fff}
.fcol h5{font-size:14px;font-weight:700;color:var(--accent);margin-bottom:20px}
.fcol li{list-style:none;display:flex;align-items:center;gap:8px;font-size:10.5px;height:31px}
.fcol svg{width:12px;height:12px;flex:none}
.social{display:flex;gap:10px}
.social span{width:21px;height:21px;border:1.4px solid var(--accent);border-radius:50%}
</style>
</head>
<body>

<!-- HERO -->
<section class="abs hero" role="img" aria-label="Photo of city high-rise towers at sunset"></section>
<header class="abs nav">
  <div class="brand"><i></i>CORVENNA</div>
  <nav class="menu"><span class="on">Home ⌄</span><span>About Us</span><span>Services ⌄</span><span>Projects ⌄</span><span>Blog</span><span>Pages ⌄</span></nav>
</header>
<div class="btn" style="left:1018px;top:38px;width:100px;height:38px">Contact Us</div>
<div class="abs center hero-copy" style="top:199px">
  <div class="eyebrow">Welcome to Corvenna</div>
  <h1 style="margin-top:12px">Inspecting builds with<br>precision and excellence</h1>
  <p style="font-size:11.5px;line-height:22px;margin-top:12px">we specialize in building inspections, fixed-price estimating and project management, with<br>independent advice from the field. Years of site experience and a commitment to quality.</p>
</div>
<div class="btn" style="left:460px;top:412px;width:123px;height:38px">Get Started <svg viewBox="0 0 12 12" fill="none" stroke="#fff" stroke-width="1.2"><circle cx="6" cy="6" r="5"/><path d="M4 6h4M6.5 4.5 8 6 6.5 7.5"/></svg></div>
<div class="ghost" style="left:604px;top:410px;width:134px;height:42px">View Projects <svg width="12" height="12" viewBox="0 0 12 12" fill="none" stroke="#fff" stroke-width="1.2"><circle cx="6" cy="6" r="5"/><path d="M4 6h4M6.5 4.5 8 6 6.5 7.5"/></svg></div>

<!-- ABOUT -->
<div class="photo" role="img" aria-label="Photo of two building inspectors in hard hats and safety vests" style="left:197px;top:645px;width:331px;height:375px;border-radius:10px;background:linear-gradient(180deg,#fff 0%,#fff 22%,#c9b79e 23%,#e6a35a 60%,#9fb4c8 100%)"></div>
<div class="abs eyebrow" style="left:600px;top:627px">About Us</div>
<h2 class="abs h2" style="left:603px;top:650px">Inspections you can<br>trust for a lifetime</h2>
<p class="abs lead" style="left:603px;top:745px;width:400px;font-size:10px">After years of building on site, we now work in the field as inspectors and coordinators. We check every stage, price your project at a fixed rate and manage trades so homes and commercial builds are finished right.</p>
<ul class="abs checks">
  <li><svg width="12" height="12" viewBox="0 0 12 12"><circle cx="6" cy="6" r="6" fill="#f9b21b"/><path d="M3.5 6.2 5.2 7.8 8.6 4.4" stroke="#fff" stroke-width="1.3" fill="none"/></svg>Building Inspections</li>
  <li><svg width="12" height="12" viewBox="0 0 12 12"><circle cx="6" cy="6" r="6" fill="#f9b21b"/><path d="M3.5 6.2 5.2 7.8 8.6 4.4" stroke="#fff" stroke-width="1.3" fill="none"/></svg>Fixed-Price Estimating</li>
  <li><svg width="12" height="12" viewBox="0 0 12 12"><circle cx="6" cy="6" r="6" fill="#f9b21b"/><path d="M3.5 6.2 5.2 7.8 8.6 4.4" stroke="#fff" stroke-width="1.3" fill="none"/></svg>Project &amp; Construction Management</li>
</ul>
<div class="btn" style="left:599px;top:994px;width:145px;height:40px">Get Free Quote</div>
<svg class="abs" style="left:758px;top:999px" width="28" height="28" viewBox="0 0 24 24" fill="none" stroke="#f9b21b" stroke-width="1.3"><path d="M5 3h4l2 5-2.5 1.5a11 11 0 0 0 6 6L16 13l5 2v4a2 2 0 0 1-2 2A16 16 0 0 1 3 5a2 2 0 0 1 2-2z"/></svg>
<div class="abs" style="left:798px;top:996px;font-size:8.5px;color:var(--muted)">call support center 24X7</div>
<div class="abs" style="left:798px;top:1012px;font-size:13px;font-weight:700">+1 555 014 2290</div>

<!-- WHY CHOOSE -->
<div class="abs center eyebrow" style="top:1103px">Why choose us?</div>
<h2 class="abs center h2" style="top:1127px">Why we're your best choice</h2>
<p class="abs center lead" style="top:1186px;font-size:10.5px">Built on decades of hands-on construction, our inspectors and estimators give home owners,<br>agents, builders and trades clear reports and fixed pricing they can rely on.</p>

<div class="card" style="left:197px;top:1260px">
  <svg width="36" height="36" viewBox="0 0 36 36" fill="none" stroke="#f9b21b" stroke-width="1.4"><path d="M18 8a8 8 0 0 0-5 14.2V26h10v-3.8A8 8 0 0 0 18 8z"/><path d="M14 30h8M18 2v3M6 14H3M33 14h-3M9 6 7 4M27 6l2-2"/></svg>
  <h3>Building Inspections</h3>
  <p>Stage, pre-purchase and handover checks. Every defect is logged with photos in a clear report you can act on.</p>
  <hr><div class="num">800+</div><small>Inspections Completed</small>
</div>
<div class="tile" role="img" aria-label="Photo of a high-rise under construction with cranes" style="left:472px;top:1260px;background:linear-gradient(180deg,#7fb8e4 0%,#c9dbe6 45%,#a08670 75%,#6e5a48 100%)"></div>
<div class="card" style="left:746px;top:1260px">
  <svg width="36" height="36" viewBox="0 0 36 36" fill="none" stroke="#f9b21b" stroke-width="1.4"><circle cx="18" cy="12" r="6"/><path d="M15 12l2 2 4-4M6 28c4 0 6-4 12-4h6M4 24l6 8M24 24c3 0 6-3 8-5"/></svg>
  <h3>Fixed-Price Estimating</h3>
  <p>Detailed quantities and cost plans for builders and trades, priced at a fixed fee with no surprises later.</p>
  <hr><div class="num">800+</div><small>Estimates Delivered</small>
</div>
<div class="tile" role="img" aria-label="Photo of a construction site at sunset with towers behind" style="left:197px;top:1590px;background:linear-gradient(180deg,#6d6f7a 0%,#d08a48 40%,#a7643a 65%,#4e3426 100%)"></div>
<div class="card" style="left:472px;top:1590px">
  <svg width="36" height="36" viewBox="0 0 36 36" fill="none" stroke="#f9b21b" stroke-width="1.4"><circle cx="20" cy="12" r="7"/><path d="M17 12h6M20 9v6M4 26c4 0 6-3 11-3h7M4 30l4 2c6 0 12-3 18-8"/></svg>
  <h3>Project Management</h3>
  <p>We coordinate trades, programs and budgets on site so your build or renovation stays on time and on cost.</p>
  <hr><div class="num">800+</div><small>Projects Managed</small>
</div>
<div class="tile" role="img" aria-label="Photo of a tower under construction with tower cranes" style="left:746px;top:1590px;background:linear-gradient(180deg,#b7c6cc 0%,#7e9aa6 50%,#3a5866 100%)"></div>

<!-- PROJECTS -->
<section class="abs projects"></section>
<div class="abs center eyebrow" style="top:2029px">Our Projects</div>
<h2 class="abs center h2" style="top:2055px">Explore our diverse range of projects</h2>
<p class="abs center lead" style="top:2113px;font-size:10.5px">We inspect, estimate and manage a wide range of projects, including residential, commercial, and<br>industrial builds.</p>
<div class="proj" role="img" aria-label="Photo of Aspen Heights towers" style="left:20px;background:linear-gradient(180deg,#5f8db5 0%,#9ab2c4 50%,#1d2a2c 100%)"><span>Aspen Heights</span></div>
<div class="proj" role="img" aria-label="Photo of Forest Hill Towers" style="left:315px;background:linear-gradient(180deg,#3e6ea4 0%,#7d8b96 50%,#1c232b 100%)"><span>Forest Hill Towers</span></div>
<div class="proj" role="img" aria-label="Photo of Bayside Residences" style="left:609px;background:linear-gradient(180deg,#7fa9d6 0%,#8f9aa2 50%,#252a2d 100%)"><span>Bayside Residences</span></div>
<div class="proj" role="img" aria-label="Photo of Parkview Plaza" style="left:904px;background:linear-gradient(180deg,#dfe6ee 0%,#3c4a5e 55%,#121a26 100%)"><span>Parkview Plaza</span></div>
<div class="btn" style="left:524px;top:2558px;width:151px;height:36px">View All Projects <svg viewBox="0 0 12 12" fill="none" stroke="#fff" stroke-width="1.2"><circle cx="6" cy="6" r="5"/><path d="M4 6h4M6.5 4.5 8 6 6.5 7.5"/></svg></div>

<!-- CTA -->
<section class="abs cta"></section>
<h2 class="abs" style="left:197px;top:2718px;font-size:36px;font-weight:700;letter-spacing:-1px;line-height:40px;color:#fff">Let's inspect your next build<br>together!</h2>
<p class="abs" style="left:197px;top:2818px;font-size:10px;line-height:18px;color:#fff">Don't leave your build to chance. Book an inspection or fixed-price estimate with Corvenna and<br>get independent advice from people who have built it themselves.</p>
<div class="btn" style="left:197px;top:2880px;width:141px;height:38px">Get Free Quote <svg viewBox="0 0 12 12" fill="none" stroke="#fff" stroke-width="1.2"><circle cx="6" cy="6" r="5"/><path d="M4 6h4M6.5 4.5 8 6 6.5 7.5"/></svg></div>
<div class="photo" role="img" aria-label="Photo of an inspector in an orange hard hat and vest pointing left" style="left:700px;top:2695px;width:300px;height:289px;background:linear-gradient(180deg,#1b2b52 0%,#c96a2a 45%,#e27a2d 100%);border-radius:140px 140px 0 0"></div>

<!-- BLOG -->
<div class="abs center eyebrow" style="top:3050px">News &amp; Tips</div>
<h2 class="abs center h2" style="top:3073px">Industry tips &amp; updates</h2>
<p class="abs center lead" style="top:3132px;font-size:10.5px">Monthly updates, site photos and practical advice for home owners, real estate agents,<br>commercial builders and trades.</p>
<article class="post" style="left:197px"><div class="img" role="img" aria-label="Photo of a building under construction with cranes" style="background:linear-gradient(180deg,#8a97a5,#b08766 60%,#6b4d38)"></div><h4>10 Things to Check in a<br>Pre-Purchase Inspection</h4><a>Read more <svg width="10" height="10" viewBox="0 0 12 12" fill="none" stroke="#f9b21b" stroke-width="1.2"><circle cx="6" cy="6" r="5"/><path d="M4 6h4M6.5 4.5 8 6 6.5 7.5"/></svg></a></article>
<article class="post" style="left:472px"><div class="img" role="img" aria-label="Photo of a concrete frame site with scaffolding" style="background:linear-gradient(180deg,#d8dde2,#9a8b80 55%,#7a3b32)"></div><h4>Why Fixed-Price Estimates<br>Help Trades Win Work</h4><a>Read more <svg width="10" height="10" viewBox="0 0 12 12" fill="none" stroke="#f9b21b" stroke-width="1.2"><circle cx="6" cy="6" r="5"/><path d="M4 6h4M6.5 4.5 8 6 6.5 7.5"/></svg></a></article>
<article class="post" style="left:746px"><div class="img" role="img" aria-label="Aerial photo of a construction site" style="background:linear-gradient(180deg,#5d6670,#8c7e70 55%,#3f4a52)"></div><h4>How Project Management<br>Keeps Your Build on Track</h4><a>Read more <svg width="10" height="10" viewBox="0 0 12 12" fill="none" stroke="#f9b21b" stroke-width="1.2"><circle cx="6" cy="6" r="5"/><path d="M4 6h4M6.5 4.5 8 6 6.5 7.5"/></svg></a></article>

<!-- CONTACT -->
<section class="abs contact"></section>
<div class="abs info">
  <svg style="margin-top:30px" width="26" height="26" viewBox="0 0 24 24" fill="none" stroke="#f9b21b" stroke-width="1.3"><path d="M5 3h4l2 5-2.5 1.5a11 11 0 0 0 6 6L16 13l5 2v4a2 2 0 0 1-2 2A16 16 0 0 1 3 5a2 2 0 0 1 2-2z"/></svg>
  <div style="font-size:10px;margin-top:6px">Call Support Center 24/7</div>
  <div style="font-size:14px;font-weight:600;margin-top:6px">+1 555 018 3347</div>
  <svg style="margin-top:16px" width="24" height="24" viewBox="0 0 24 24" fill="none" stroke="#f9b21b" stroke-width="1.3"><path d="M3 10l9-6 9 6v10H3z"/><path d="M3 10l9 6 9-6"/></svg>
  <div style="font-size:10px;margin-top:6px">Write To Us</div>
  <div style="font-size:14px;font-weight:600;margin-top:6px">hello@corvenna-mail.com</div>
  <div role="img" aria-label="Photo of a support agent with a headset" style="position:absolute;left:73px;top:236px;width:110px;height:152px;border-radius:55px 55px 0 0;background:linear-gradient(180deg,#1b2b52,#e9e6e2 60%,#f3f1ee)"></div>
</div>
<div class="abs form">
  <div class="abs eyebrow" style="left:31px;top:32px">Contact Us</div>
  <h2 class="abs" style="left:31px;top:52px;font-size:32px;font-weight:700;letter-spacing:-1px">Get in touch with us</h2>
  <div class="field" style="left:31px;top:130px;width:226px;padding-left:10px">Enter Your Name</div>
  <div class="field" style="left:273px;top:130px;width:226px;padding-left:10px">Enter Your Email</div>
  <div class="field" style="left:31px;top:180px;width:226px;padding-left:10px">Phone Number</div>
  <div class="field" style="left:273px;top:180px;width:226px;padding-left:10px">Subject</div>
  <div class="field" style="left:31px;top:229px;width:468px;height:55px;padding-left:10px">Message</div>
  <div class="btn" style="left:31px;top:315px;width:79px;height:31px">Submit</div>
</div>

<!-- FOOTER -->
<footer class="abs footer">
  <div class="abs brand" style="left:197px;top:78px;font-size:24px;font-weight:800"><i style="width:24px;height:24px"></i>CORVENNA</div>
  <p class="abs" style="left:197px;top:143px;width:180px;font-size:9.5px;line-height:17px">Independent inspections, estimating and project management that give you peace of mind at every stage.</p>
  <div class="abs fcol" style="left:402px;top:68px"><h5>Our Services</h5><ul>
    <li><svg viewBox="0 0 12 12" fill="none" stroke="#f9b21b" stroke-width="1.2"><circle cx="6" cy="6" r="5"/><path d="M4 6h4M6.5 4.5 8 6 6.5 7.5"/></svg>Building Inspections</li>
    <li><svg viewBox="0 0 12 12" fill="none" stroke="#f9b21b" stroke-width="1.2"><circle cx="6" cy="6" r="5"/><path d="M4 6h4M6.5 4.5 8 6 6.5 7.5"/></svg>Estimating Services</li>
    <li><svg viewBox="0 0 12 12" fill="none" stroke="#f9b21b" stroke-width="1.2"><circle cx="6" cy="6" r="5"/><path d="M4 6h4M6.5 4.5 8 6 6.5 7.5"/></svg>Project Management</li>
    <li><svg viewBox="0 0 12 12" fill="none" stroke="#f9b21b" stroke-width="1.2"><circle cx="6" cy="6" r="5"/><path d="M4 6h4M6.5 4.5 8 6 6.5 7.5"/></svg>Construction Management</li>
    <li><svg viewBox="0 0 12 12" fill="none" stroke="#f9b21b" stroke-width="1.2"><circle cx="6" cy="6" r="5"/><path d="M4 6h4M6.5 4.5 8 6 6.5 7.5"/></svg>Fixed Pricing</li></ul></div>
  <div class="abs fcol" style="left:605px;top:68px"><h5>Company</h5><ul>
    <li><svg viewBox="0 0 12 12" fill="none" stroke="#f9b21b" stroke-width="1.2"><circle cx="6" cy="6" r="5"/><path d="M4 6h4M6.5 4.5 8 6 6.5 7.5"/></svg>About Us</li>
    <li><svg viewBox="0 0 12 12" fill="none" stroke="#f9b21b" stroke-width="1.2"><circle cx="6" cy="6" r="5"/><path d="M4 6h4M6.5 4.5 8 6 6.5 7.5"/></svg>Services</li>
    <li><svg viewBox="0 0 12 12" fill="none" stroke="#f9b21b" stroke-width="1.2"><circle cx="6" cy="6" r="5"/><path d="M4 6h4M6.5 4.5 8 6 6.5 7.5"/></svg>Industry Tips</li>
    <li><svg viewBox="0 0 12 12" fill="none" stroke="#f9b21b" stroke-width="1.2"><circle cx="6" cy="6" r="5"/><path d="M4 6h4M6.5 4.5 8 6 6.5 7.5"/></svg>Faqs</li></ul></div>
  <div class="abs fcol" style="left:810px;top:68px"><h5>Contact Us</h5><ul>
    <li><svg viewBox="0 0 24 24" fill="none" stroke="#f9b21b" stroke-width="1.6"><path d="M5 3h4l2 5-2.5 1.5a11 11 0 0 0 6 6L16 13l5 2v4a2 2 0 0 1-2 2A16 16 0 0 1 3 5a2 2 0 0 1 2-2z"/></svg>+1 555 018 3347</li>
    <li><svg viewBox="0 0 24 24" fill="none" stroke="#f9b21b" stroke-width="1.6"><path d="M3 10l9-6 9 6v10H3z"/><path d="M3 10l9 6 9-6"/></svg>hello@corvenna-mail.com</li>
    <li style="height:auto;align-items:flex-start;line-height:17px;padding-top:6px"><svg viewBox="0 0 24 24" fill="none" stroke="#f9b21b" stroke-width="1.6"><rect x="3" y="4" width="18" height="16"/><path d="M3 9h18"/></svg>48 Harbour Row Lane<br>Kessel Street 14B, 4102 QL</li></ul></div>
  <div class="abs" style="left:197px;top:300px;width:806px;border-top:1px solid rgba(255,255,255,.12)"></div>
  <div class="abs" style="left:197px;top:318px;font-size:10px">Copyright © 2024 Corvenna Australia Pty Ltd. All Rights Reserved.</div>
  <div class="abs social" style="left:852px;top:313px"><span></span><span></span><span></span><span></span><span></span></div>
  <div class="abs" style="left:197px;top:350px;width:806px;border-top:1px solid rgba(255,255,255,.12)"></div>
</footer>

</body>
</html>
```